Harborline Advisory - Vocanet Header

I am a solopreneur with a consulting company. I do management consulting for small and mid-size manufacturers. There are two ways my prospects check me out - my web page, which went live this week (www.harborlineadvisory.example), and my personal Vocanet page. I'm working on my Vocanet page now, and I'd like to have a header image that is unique and aligned with my brand.

My clients are smaller manufacturers, typically with 50-400 people. They are privately held, often by an individual or family, but sometimes by a professional investment group. They aren't as sophisticated as the Crestmark 700 guys, and sometimes they struggle to grow because their processes break, or they don't have the right people or something else like that. I help them get through those issues.

Many of the people visiting the site will have a technical/engineering orientation, and most are in their late 40's to early 60's.

From my research, I think the image for my personal page is 1584x396, and this will be my primary page. The business page has a banner image size of 1536x768. I'd like to be able to use the same image in both.

Target Market(s)

Small and Mid-size manufacturers - C-Suite executives

Industry/Entity Type

Manufacturing

Font styles to use
Sans Serif

Colors

Designer to choose colors to be used in the design.

Requirements
Must have
• Logo incorporated. Be adaptable to both my personal Vocanet page and Business page, which have slightly different sizes.

```html
<!DOCTYPE html>
<html lang="en">
<head>
<meta charset="utf-8">
<title>Harborline Vocanet Banner</title>
<link href="https://fonts.googleapis.com/css2?family=Open+Sans:wght@400;700&family=Arimo:wght@700&display=swap" rel="stylesheet">
<style>
  :root {
    --navy: #1b2463;
    --navy-deep: #151d57;
    --navy-shadow: #0c1248;
    --gold: #e0952a;
    --white: #ffffff;
    --label: #555a66;
    --sheet: #f3f3f3;
    --photo-warm: #a8845f;
    --photo-cool: #c9ccd3;
  }
  * { margin: 0; padding: 0; box-sizing: border-box; }
  html, body { width: 1200px; height: 1200px; overflow: hidden; }
  body {
    position: relative;
    background: radial-gradient(ellipse at center, #ffffff 0%, var(--sheet) 75%);
    font-family: "Arimo", Arial, sans-serif;
  }
  .sheet-title {
    position: absolute; top: 42px; left: 0; width: 1200px;
    text-align: center;
    font-family: "Open Sans", Arial, sans-serif;
    font-weight: 700; font-size: 29px; letter-spacing: 0.5px;
    color: var(--navy);
  }
  .size-label {
    position: absolute; left: 24px;
    font-family: "Open Sans", Arial, sans-serif;
    font-size: 15px; color: var(--label);
  }
  .banner {
    position: absolute; left: 25px;
    background: linear-gradient(180deg, var(--navy) 0%, var(--navy-deep) 100%);
    box-shadow: 2px 3px 6px rgba(0,0,0,0.18);
    overflow: hidden;
  }
  .banner::after {
    content: ""; position: absolute; inset: 7px;
    border: 1px solid rgba(255,255,255,0.07);
  }
  .banner--profile { top: 150px; width: 1117px; height: 280px; }
  .banner--business { top: 519px; width: 1148px; height: 574px; }
  .headline {
    position: absolute; text-align: center; font-weight: 700;
    text-transform: uppercase; line-height: 1;
  }
  .headline__lead { color: var(--gold); font-size: 35px; letter-spacing: 0.3px; }
  .headline__sub {
    display: flex; align-items: center; justify-content: center; gap: 8px;
    margin-top: 6px; color: var(--white); font-size: 35px; letter-spacing: -0.3px;
  }
  .headline__sub::before, .headline__sub::after {
    content: ""; width: 62px; height: 2px; background: var(--white);
  }
  .banner--profile .headline { left: 159px; top: 254px; top: 104px; width: 560px; }
  .banner--business .headline { left: 82px; top: 253px; width: 540px; }
  .banner--business .headline__sub { gap: 14px; }
  .banner--business .headline__sub::before,
  .banner--business .headline__sub::after { width: 60px; }
  .photo-frame {
    position: absolute; border-radius: 50%;
    border: solid var(--white);
    box-shadow: -10px 6px 0 var(--navy-shadow);
  }
  .photo {
    width: 100%; height: 100%; border-radius: 50%;
    background: radial-gradient(circle at 40% 45%, var(--photo-cool) 0%, var(--photo-warm) 55%, #5b4a3c 100%);
  }
  .banner--profile .photo-frame { left: 712px; top: 24px; width: 232px; height: 232px; border-width: 28px; }
  .banner--business .photo-frame { left: 680px; top: 56px; width: 400px; height: 400px; border-width: 46px; }
  .brand-name {
    position: absolute; color: var(--white); font-weight: 700;
    text-transform: uppercase; line-height: 1.15; letter-spacing: 1px;
  }
  .banner--profile .brand-name { left: 962px; top: 116px; font-size: 19px; }
  .banner--business .brand-name { left: 680px; top: 486px; width: 400px; text-align: center; font-size: 24px; }
  .footer-rule {
    position: absolute; left: 0; bottom: 0; width: 1200px; height: 6px;
    background: var(--gold);
  }
</style>
</head>
<body>
  <h1 class="sheet-title">HARBORLINE VOCANET BANNER</h1>

  <p class="size-label" style="top:112px">1584X396</p>
  <section class="banner banner--profile">
    <div class="headline">
      <div class="headline__lead">Enabling Manufacturers</div>
      <div class="headline__sub">To Break Through</div>
    </div>
    <div class="photo-frame">
      <div class="photo" role="img" aria-label="Photo of a team gathered around a table reviewing documents and charts"></div>
    </div>
    <div class="brand-name">Harborline<br>Advisory</div>
  </section>

  <p class="size-label" style="top:479px">1536X768</p>
  <section class="banner banner--business">
    <div class="headline">
      <div class="headline__lead">Enabling Manufacturers</div>
      <div class="headline__sub">To Break Through</div>
    </div>
    <div class="photo-frame">
      <div class="photo" role="img" aria-label="Photo of a team gathered around a table reviewing documents and charts"></div>
    </div>
    <div class="brand-name">Harborline Advisory</div>
  </section>

  <div class="footer-rule"></div>
</body>
</html>
```